Business card design for a world class martial arts and group fitness facility

We need a professional and eye catching design for a business card. The card will be used in networking as well as marketing.
We are a martial arts facility offering Taekwondo, Brazilian Jiu Jitsu, and group fitness. All of our programs are geared for kids and adults.
Our Taekwondo program is lead by a Hall of Fame instructor who was Instructor of the Year in 2015.
Our Brazilian Jiu Jitsu program is lead by a wold class instructor who is also a part of the renown Brazilian KVO team.
We offer 3 focused group fitness programs: Ring striking, Pulse Fitness, and The Meadow which are all lead by certified instructors in a small group setting.
Our facility is state of the art and has been recognized as such in nationally published magazines.
Our business is named The Lantern which is the linear logo that is attached. This is the main logo. I also attached a circular logo we have used in some marketing material. Our Jiu Jitsu program is the KVO team logo. The Taekwondo program is the TORVEX Prime. It would be nice to somehow incorporate all 3 logos, but The Lantern is most important.
Industry/Entity Type
Martial Art
Contact Information for Business Card
We would like to use all 3 logos if possible but The Lantern is the most important. We would like to have a place for a staff member's name while keeping the focus on the programs we offer.
Look and feel
Each slider illustrates characteristics of the customer's brand and the style your logo design should communicate.

```html
<!DOCTYPE html>
<html lang="en">
<head>
<meta charset="utf-8">
<title>The Lantern – Business Card</title>
<link rel="stylesheet" href="https://fonts.googleapis.com/css2?family=Open+Sans:wght@400;600;700&display=swap">
<style>
  :root {
    --backdrop: #3a3430;
    --card: #0d0d0d;
    --card-edge: #1a1a1a;
    --ink: #e9e9e9;
    --ink-soft: #bdbdbd;
    --rule: #2a2a2a;
    --badge-red: #c0262d;
    --badge-navy: #1f2a5c;
  }
  * { margin: 0; padding: 0; box-sizing: border-box; }
  html, body {
    width: 1200px; height: 900px; overflow: hidden;
    background: var(--backdrop);
    font-family: "Open Sans", Arial, sans-serif;
    color: var(--ink);
  }
  .stage {
    position: relative; width: 1200px; height: 900px;
    display: flex; align-items: center; justify-content: center; gap: 50px;
  }
  .card {
    position: relative;
    width: 525px; height: 300px;
    background: var(--card);
    border: 1px solid var(--card-edge);
    box-shadow: 0 10px 30px rgba(0,0,0,.45);
  }
  /* Front */
  .card-front { display: flex; }
  .front-brand {
    width: 50%;
    display: flex; align-items: center; justify-content: center; gap: 12px;
  }
  .brand-mark {
    width: 22px; height: 22px; border-radius: 50%;
    background: var(--ink);
  }
  .brand-name {
    font-weight: 700; font-size: 32px; color: var(--ink);
    letter-spacing: .5px;
  }
  .front-divider {
    position: absolute; left: 50%; top: 55px; bottom: 55px;
    width: 1px; background: var(--rule);
  }
  .front-details {
    width: 50%; padding: 58px 0 0 28px;
  }
  .staff-name { font-weight: 700; font-size: 16px; }
  .staff-title { font-size: 13px; color: var(--ink-soft); margin-bottom: 14px; }
  .address { font-size: 13px; line-height: 1.35; margin-bottom: 14px; }
  .contact-list { list-style: none; font-size: 13px; line-height: 1.55; }
  .contact-list li { display: flex; align-items: center; gap: 10px; }
  .contact-list svg { width: 10px; height: 10px; fill: var(--ink); flex: none; }
  /* Back */
  .card-back {
    display: flex; flex-direction: column; align-items: center; justify-content: center;
  }
  .back-brand { display: flex; align-items: center; gap: 12px; margin-bottom: 30px; }
  .partner-badges {
    position: absolute; right: 120px; bottom: 58px;
    display: flex; gap: 14px; align-items: center;
  }
  .badge-round {
    width: 56px; height: 56px; border-radius: 50%;
    background: #141414; border: 3px solid var(--badge-red);
  }
  .badge-square {
    width: 60px; height: 60px;
    background: var(--badge-navy); border: 2px solid #d8d8d8;
  }
</style>
</head>
<body>
<main class="stage">
  <section class="card card-front" aria-label="Business card front">
    <div class="front-brand">
      <span class="brand-mark"></span>
      <span class="brand-name">The Lantern</span>
    </div>
    <div class="front-divider"></div>
    <div class="front-details">
      <p class="staff-name">Daniel Mercer</p>
      <p class="staff-title">Managing Director</p>
      <p class="address">12345, Address Goes Here<br>Country Name, 123456.</p>
      <ul class="contact-list">
        <li><svg viewBox="0 0 10 10"><path d="M2 0.5 L3.6 2.6 L2.8 3.6 C3.4 5 4.9 6.5 6.4 7.2 L7.4 6.4 L9.5 8 L8.4 9.5 C4.5 9.2 0.8 5.5 0.5 1.6 Z"/></svg>044-555 019 284</li>
        <li><svg viewBox="0 0 10 10"><path d="M0.5 2 H9.5 V8.5 H0.5 Z M1.2 2.6 L5 5.6 L8.8 2.6" stroke="#0d0d0d" stroke-width=".8"/></svg>info@lanterndojo.com</li>
        <li><svg viewBox="0 0 10 10"><circle cx="5" cy="5" r="4.5"/><path d="M0.5 5 H9.5 M5 0.5 C3 3 3 7 5 9.5 M5 0.5 C7 3 7 7 5 9.5" stroke="#0d0d0d" stroke-width=".7" fill="none"/></svg>www.lanterndojo.com</li>
      </ul>
    </div>
  </section>

  <section class="card card-back" aria-label="Business card back">
    <div class="back-brand">
      <span class="brand-mark"></span>
      <span class="brand-name">The Lantern</span>
    </div>
    <div class="partner-badges">
      <span class="badge-round" role="img" aria-label="KVO team badge"></span>
      <span class="badge-square" role="img" aria-label="TORVEX Prime badge"></span>
    </div>
  </section>
</main>
</body>
</html>
```